Marlo Vista Table & Chair Rentals

We need a business card for a table and chair rental company. We rent tables and chairs for weddings, funerals, business events and parties. We want something that looks clean and elegant while not being too busy. We would like colors in the green and blue hues and avoiding anything orange. We want to make sure the font is large enough to be seen easily.

Target Market(s)

Wedding & Event Rentals

Industry/Entity Type

Events

Contact Information for Business Card

Marlo Vista, sales@marlovistarentals.example, marlovistarentals.example, 360-555-0182

Requirements
Must have
• Easy to read font
Should not have
• Orange anywhere in the design

```html
<!DOCTYPE html>
<html lang="en">
<head>
<meta charset="utf-8">
<title>Marlo Vista Table &amp; Chair Rentals — Business Card</title>
<link rel="stylesheet" href="https://fonts.googleapis.com/css2?family=Courgette&family=Open+Sans:wght@400&family=Arimo:wght@400&display=swap">
<style>
  :root {
    --page-bg: #e9e7e3;
    --card-edge: #3a3029;
    --card-white: #ffffff;
    --ink: #2b2420;
    --band: rgba(92, 80, 72, 0.86);
    --band-text: #ffffff;
    --photo-dark: #3f3a2c;
    --photo-green: #6f7a52;
    --photo-light: #d9d9d2;
    --photo-bloom: #c9d6de;
  }
  * { margin: 0; padding: 0; box-sizing: border-box; }
  html, body { width: 1200px; height: 900px; overflow: hidden; }
  body {
    background: var(--page-bg);
    display: flex;
    flex-direction: column;
    align-items: center;
    justify-content: center;
    gap: 40px;
  }
  .card {
    position: relative;
    width: 700px;
    height: 400px;
    border: 9px solid var(--card-edge);
    overflow: hidden;
    box-shadow: 0 6px 18px rgba(0,0,0,0.18);
  }

  /* Front */
  .card--front { background: var(--photo-dark); }
  .front-photo {
    position: absolute; inset: 0;
    background:
      radial-gradient(ellipse 22% 30% at 68% 55%, var(--photo-bloom) 0%, rgba(201,214,222,0) 100%),
      radial-gradient(ellipse 18% 22% at 20% 62%, var(--photo-light) 0%, rgba(217,217,210,0) 100%),
      radial-gradient(ellipse 40% 35% at 80% 15%, #eeeeea 0%, rgba(238,238,234,0) 100%),
      linear-gradient(160deg, #8b8a78 0%, var(--photo-green) 40%, var(--photo-dark) 100%);
  }
  .front-band { position: absolute; inset: 0; }
  .front-title {
    position: absolute;
    left: 205px; top: 150px;
    transform: rotate(-27deg);
    transform-origin: left top;
    color: var(--band-text);
  }
  .front-title .brand-name {
    font-family: "Courgette", cursive;
    font-size: 40px;
    line-height: 1;
  }
  .front-title .tagline {
    font-family: "Open Sans", sans-serif;
    font-size: 17px;
    letter-spacing: 0.5px;
    margin-top: 4px;
    margin-left: 18px;
  }

  /* Back */
  .card--back {
    background: var(--card-white);
    display: flex;
    align-items: center;
    padding-left: 50px;
    padding-right: 36px;
  }
  .back-name {
    font-family: "Courgette", cursive;
    font-size: 46px;
    line-height: 1;
    color: var(--ink);
    white-space: nowrap;
    flex: 0 0 250px;
    margin-top: 90px;
  }
  .back-divider {
    flex: 0 0 14px;
    height: 120px;
    margin: 20px 22px 0 24px;
  }
  .contact-list {
    list-style: none;
    font-family: "Arimo", sans-serif;
    color: var(--ink);
    font-size: 17px;
    line-height: 1.35;
    white-space: nowrap;
    margin-top: -50px;
  }
  .contact-list .phone { font-size: 20px; letter-spacing: 1px; }
</style>
</head>
<body>

<section class="card card--front" aria-label="Card front">
  <div class="front-photo" role="img" aria-label="Soft-focus photo of white and pale blue wedding flowers beside white chairs in a garden"></div>
  <svg class="front-band" viewBox="0 0 682 382" preserveAspectRatio="none" aria-hidden="true">
    <polygon points="0,300 682,-50 682,60 0,410" fill="var(--band)"/>
    <line x1="500" y1="0" x2="682" y2="320" stroke="var(--card-edge)" stroke-width="5"/>
  </svg>
  <div class="front-title">
    <div class="brand-name">Marlo Vista</div>
    <div class="tagline">Table and Chair Rentals</div>
  </div>
</section>

<section class="card card--back" aria-label="Card back">
  <div class="back-name">Marlo Vista</div>
  <svg class="back-divider" viewBox="0 0 14 120" aria-hidden="true">
    <line x1="7" y1="0" x2="7" y2="120" stroke="var(--ink)" stroke-width="1.5"/>
    <polygon points="7,30 11,60 7,90 3,60" fill="var(--ink)"/>
  </svg>
  <ul class="contact-list">
    <li class="phone">360-555-0182</li>
    <li>sales@marlovistarentals.example</li>
    <li>www.marlovistarentals.example</li>
  </ul>
</section>

</body>
</html>
```